Calling All Web Design Visionaries: Transform the Meridian Vault Website!

Dear Web Design Innovators,

Are you ready to embark on a cosmic design journey? We are thrilled to announce an exciting opportunity to revamp and upgrade the Meridian Vault website, and we need your exceptional design prowess to bring our vision to life.

About Meridian Vault:
Meridian Vault is on a mission to reshape the future of space construction. We're pioneers in the field, developing cutting-edge concept construction blocks that promise to redefine how we build beyond our planet's boundaries. Our solutions are scalable, sustainable, and poised to accelerate humanity's journey into the cosmos.

Current Website:
Take a look at our current website [www.meridianvault-example.co.uk](https://www.meridianvault-example.co.uk) to get a glimpse of our existing online presence. While it served us well, we believe it's time for a transformative makeover.

Your Mission:
We're seeking imaginative web designers who can bring a fresh perspective to our online platform. Here's the website layout we're envisioning:
- Homepage: A futuristic and clean design that reflects our commitment to innovation. Clear navigation to key sections.
- About Us: A captivating section introducing our mission and team.
- Products: Highlighting our revolutionary concept construction blocks.
- Projects: Showcasing our involvement in space construction initiatives.
- Blog: A space to share our insights, progress, and news.
- Contact: Easy access for potential partners and investors to reach out.

Image Suggestions:
- Celestial imagery, cosmic landscapes, and space construction concepts can add a captivating visual element.
- Incorporate a color palette that combines deep space blues with modern metallic tones for a futuristic feel.
- Use high-quality images and graphics that convey the excitement and possibilities of space construction.

Why You Should Join Us:
By taking on this challenge, you'll have the chance to contribute to a groundbreaking mission and be part of the future of space exploration. Your design will be seen by space enthusiasts, investors, and industry experts worldwide.

If you're ready to embark on this cosmic design journey with us, please submit your portfolio and a brief introduction by 22/09/23. We can't wait to see your visionary concepts.

Let's transform the Meridian Vault website into a space of inspiration and innovation. Join us on this incredible adventure!

Best regards,

Tobi
Updates

Target Market(s)

Orbit Service providers, Governments, Space Agencies. Space Infrastructure

Industry/Entity Type

Space, Technology, Innovation, Architecture. Construction

Coding

Coded - Design and coding required

Number of Pages Required

5+ page

Colors
0054AA
0677BA
7BADD7
CADEEF
E8F1F8
6B429C
8869AF
B7A5CE
E3DAEB
F3F0F8

Requirements
Must have
• The logos i have outlined in the website revamp doc, i also need a sub section for FAQs terms of service etc like most professional websites. A page to sell merch. Like our custom hoody, t shirt, key rings, hats, joggers, etc
Nice to have
• any case studies of satellite innovations reaching project completion and how they might relate to my project.

```html
<!DOCTYPE html>
<html lang="en">
<head>
<meta charset="utf-8">
<title>Meridian Vault — Invest in the Future</title>
<link href="https://fonts.googleapis.com/css2?family=Exo+2:wght@500;600;700&family=Saira:wght@400;500;600&display=swap" rel="stylesheet">
<style>
:root{
  --blue:#0054AA;
  --blue-mid:#0677BA;
  --blue-soft:#7BADD7;
  --blue-pale:#CADEEF;
  --band:#E8F1F8;
  --page:#F3F7FC;
  --ink:#111821;
  --ink-soft:#3a4350;
  --white:#ffffff;
  --space:#071226;
}
*{box-sizing:border-box;margin:0;padding:0}
html,body{width:1200px;height:4043px;overflow:hidden}
body{background:var(--page);font-family:"Saira",sans-serif;color:var(--ink);position:relative}
.abs{position:absolute}
h1,h2,h3{font-family:"Exo 2",sans-serif;font-weight:700;text-transform:uppercase;letter-spacing:.3px}
.accent{color:var(--blue)}
.btn{display:inline-flex;align-items:center;justify-content:center;font-family:"Exo 2",sans-serif;font-weight:700;font-size:12px;text-transform:uppercase;letter-spacing:.3px;text-decoration:none;border:0}
.btn-blue{background:var(--blue);color:var(--white)}
.btn-pale{background:var(--blue-pale);color:var(--blue)}
.rule{display:inline-block;height:1px;background:var(--blue);width:50px;vertical-align:middle}
.section-title{position:absolute;left:0;width:1200px;text-align:center;font-size:29px;color:var(--ink)}
.section-title .rule{margin:0 16px}

/* hero */
.hero{left:0;top:0;width:1200px;height:675px;background:linear-gradient(160deg,#0a1a38 0%,#123a6e 40%,#0a2249 70%,#040a16 100%)}
.nav{left:121px;top:24px;width:958px;height:83px;background:rgba(150,158,168,.78);display:flex;align-items:center;padding:0 15px 0 16px}
.brand{display:flex;align-items:center;gap:10px;font-family:"Exo 2",sans-serif;font-weight:700;font-size:17px;color:#e9edf2;text-transform:uppercase;line-height:1}
.brand-mark{width:22px;height:22px;border-radius:50%;background:#dfe4ea;flex:none}
.nav-links{margin-left:auto;display:flex;align-items:center;height:100%}
.nav-links a{color:#eef2f6;text-decoration:none;font-size:12px;font-family:"Exo 2",sans-serif;font-weight:600;text-transform:uppercase;margin-right:40px;height:100%;display:flex;align-items:center}
.nav-links a.current{color:#fff;border-top:1px solid #fff;border-bottom:1px solid #fff;height:83px}
.nav-links a.btn{margin-right:0;width:121px;height:37px}
.hero-copy{left:195px;top:308px;width:440px;color:#fff}
.hero-copy h1{font-size:38px;line-height:1.1;margin-bottom:12px;white-space:nowrap}
.hero-copy p{font-size:15px;line-height:1.5;color:#e6ecf4;width:420px}
.hero-btns{left:195px;top:428px;display:flex;gap:16px}
.hero-btns .btn{height:36px;width:143px}

/* about */
.about-art{left:122px;top:748px;width:462px;height:402px}
.eyebrow{font-size:12px;letter-spacing:1px;color:var(--blue);text-transform:uppercase;font-weight:500}
.about-title{left:659px;top:824px;font-size:29px;display:flex;align-items:center}
.about-title .rule{width:112px;margin-left:16px}
.about-sub{left:687px;top:886px;font-weight:600;font-size:15px}
.about-text{left:687px;top:924px;width:385px;font-size:14.5px;line-height:25.5px;color:var(--ink-soft)}
.about-btn{left:658px;top:1051px;width:143px;height:35px}

/* horizon panel */
.horizon{left:121px;top:1225px;width:958px;height:339px;border-radius:4px;background:linear-gradient(100deg,var(--blue) 0%,#0d4a93 45%,#17325a 75%,#121c2d 100%);color:#fff;padding:50px 44px 0}
.horizon h2{font-size:28px;display:flex;align-items:center;gap:12px;margin-bottom:18px}
.horizon h2 .rule{background:#c7d8ee;width:112px}
.ticks{list-style:none}
.ticks li{position:relative;padding-left:31px;font-size:14.5px;line-height:23px;margin-bottom:22px;max-width:790px}
.ticks li svg{position:absolute;left:0;top:6px}
.ticks b{font-weight:600}
.horizon .ticks li{color:#e8f0fb}

/* building blocks */
.band{left:0;top:1915px;width:1200px;height:419px;background:var(--band)}
.block-card{top:1689px;width:375px;height:300px;border-radius:4px;overflow:hidden}
.block-card .fill{position:absolute;inset:0}
.block-card h3{position:absolute;left:0;right:0;text-align:center;color:#fff;font-size:18px}
.block-card p{position:absolute;left:30px;right:30px;text-align:center;color:#e2ecf8;font-size:13px;line-height:20px}

/* invest */
.invest-list{left:215px;top:2108px;width:770px}
.invest-list li{color:var(--ink-soft);margin-bottom:22px;max-width:770px}
.invest-list b{color:var(--ink)}

/* journey */
.post{top:2461px;width:304px;height:339px;background:var(--band)}
.post .pic{position:absolute;left:0;top:0;width:304px;height:224px}
.post .date{position:absolute;left:14px;top:12px;color:#fff;font-size:11.5px}
.post p{position:absolute;left:22px;right:22px;top:250px;text-align:center;font-size:15px;line-height:21px;font-weight:500;color:var(--ink)}
.post .go{position:absolute;left:136px;top:318px;width:34px;height:34px;border-radius:50%;background:var(--band);display:flex;align-items:center;justify-content:center}
.post.featured{background:var(--blue)}
.post.featured p{color:#fff}
.post.featured .go{background:#fff}
.view-all{left:529px;top:2850px;width:143px;height:36px}

/* community */
.community{left:121px;top:2962px;width:958px;height:299px;border-radius:4px;background:linear-gradient(180deg,#0c58ac,#0a4d98);color:#fff;text-align:center}
.community h2{position:absolute;left:0;right:0;top:62px;font-size:29px}
.community h2 .rule{background:#c6d8ef;width:50px;margin:0 16px}
.community p{position:absolute;left:0;right:0;top:106px;font-size:15px;line-height:23px;color:#e6eef9}
.signup{position:absolute;left:201px;top:183px;width:552px;height:42px;background:rgba(205,222,239,.35);display:flex}
.signup span{flex:1;text-align:left;padding-left:17px;line-height:42px;font-size:13px;color:#e8eff8}
.signup .btn{width:129px;height:36px;margin:3px;background:var(--blue-pale);color:var(--blue)}

/* contact */
.field{height:36px;background:var(--band);border:1px solid #dde7f1;font-size:12.5px;color:var(--ink);padding:10px 15px}
.field.msg{height:149px}
.send{left:529px;top:3658px;width:143px;height:36px}

/* footer */
.footer{left:0;top:3768px;width:1200px;height:230px;background:var(--blue);color:#fff}
.footer-brand{left:121px;top:3830px;font-family:"Exo 2",sans-serif;font-weight:700;font-size:22px;line-height:1.1;display:flex;align-items:center;gap:10px;text-transform:uppercase;color:#fff}
.footer-brand .brand-mark{background:#fff;width:26px;height:26px}
.socials{left:121px;top:3925px;display:flex;gap:8px}
.socials span{width:34px;height:34px;background:#1c64b5;display:block}
.socials span.on{background:#fff}
.quick{color:#fff}
.quick h3{font-size:18px;display:flex;align-items:center;gap:12px;margin-bottom:8px}
.quick h3 .rule{background:#cfe0f3;width:57px}
.quick ul{list-style:none;display:grid;grid-template-columns:113px 110px;row-gap:6px}
.quick a{color:#eaf1fa;text-decoration:none;font-size:12.5px}
.map{left:612px;top:3815px;width:467px;height:143px;background:linear-gradient(90deg,#a4d8d6,#c6e4c8 50%,#aadcee 100%)}
.legal{left:0;top:3998px;width:1200px;height:45px;background:#004a98;color:#dfe9f6;font-size:11px;display:flex;align-items:center;padding:0 121px}
.legal .faint{color:#7ea6d4;margin-left:70px}
.legal .links{margin-left:auto}
.legal a{color:#7BADD7;text-decoration:none}
</style>
</head>
<body>

<header>
  <div class="abs hero" role="img" aria-label="Photograph of Earth at night seen from orbit against a starfield"></div>
  <nav class="abs nav">
    <div class="brand"><span class="brand-mark"></span>Meridian Vault</div>
    <div class="nav-links">
      <a href="#" class="current">Home</a>
      <a href="#">About Us</a>
      <a href="#">Products</a>
      <a href="#">Projects</a>
      <a href="#">Blog</a>
      <a href="#" class="btn btn-blue">Contact Us</a>
    </div>
  </nav>
  <div class="abs hero-copy">
    <h1>Invest in the Future</h1>
    <p>There is a brand-new frontier opening to mankind, and the possibilities are endless.</p>
  </div>
  <div class="abs hero-btns">
    <a href="#" class="btn btn-blue">Explore More</a>
    <a href="#" class="btn btn-pale">Enquiry Now</a>
  </div>
</header>

<section>
  <svg class="abs about-art" viewBox="0 0 462 402" role="img" aria-label="Hexagonal photo collage of a lunar surface, Earth from space and a spacecraft">
    <defs>
      <linearGradient id="hexFill" x1="0" y1="0" x2="1" y2="1">
        <stop offset="0" stop-color="#6f7784"/>
        <stop offset=".5" stop-color="#1d3a64"/>
        <stop offset="1" stop-color="#070d1a"/>
      </linearGradient>
    </defs>
    <polygon points="115,0 347,0 462,201 347,402 115,402 0,201" fill="url(#hexFill)"/>
  </svg>
  <p class="abs eyebrow" style="left:659px;top:798px">Who are we?</p>
  <h2 class="abs about-title"><span>About <span class="accent">Us</span></span><span class="rule"></span></h2>
  <p class="abs about-sub">Redefining the Boundaries of Space</p>
  <p class="abs about-text">In an industry where history and reputation often take centre stage, we're the fresh face poised to redefine the rules. Meet The Meridian Vault—a newcomer with a vision that's nothing short of revolutionary.</p>
  <a href="#" class="abs btn btn-blue about-btn">Explore More</a>
</section>

<section class="abs horizon">
  <h2>Exploring the Cosmic Horizon <span class="rule"></span></h2>
  <ul class="ticks">
    <li><svg width="16" height="10" viewBox="0 0 16 10"><path d="M1 5l3 3 6-7M6 8l1 1 8-8" fill="none" stroke="#fff" stroke-width="1.3"/></svg><b>Project Vision:</b> An in-depth exploration of my project's vision, including its long-term goals and impact on the space industry.</li>
    <li><svg width="16" height="10" viewBox="0 0 16 10"><path d="M1 5l3 3 6-7M6 8l1 1 8-8" fill="none" stroke="#fff" stroke-width="1.3"/></svg><b>Space Industry Insights:</b> A section discussing the current state of the space industry and how my project fits into the larger context.</li>
    <li><svg width="16" height="10" viewBox="0 0 16 10"><path d="M1 5l3 3 6-7M6 8l1 1 8-8" fill="none" stroke="#fff" stroke-width="1.3"/></svg><b>Future Scenarios:</b> Imaginative scenarios of what the future could look like with The Meridian Vault's success.</li>
  </ul>
</section>

<div class="abs band"></div>
<h2 class="section-title" style="top:1630px"><span class="rule"></span>Building Blocks of <span class="accent">The Future</span><span class="rule"></span></h2>
<article class="abs block-card" style="left:215px">
  <div class="fill" role="img" aria-label="Illustration of a glowing atom model on a blue background" style="background:linear-gradient(180deg,#2d7fc0 0%,#0d4a93 100%)"></div>
  <h3 style="top:256px">VaultBlocks</h3>
</article>
<article class="abs block-card" style="left:610px">
  <div class="fill" role="img" aria-label="Photograph of a space station module orbiting above Earth" style="background:linear-gradient(180deg,#3a6ea8 0%,#0b4f9e 100%)"></div>
  <h3 style="top:197px">Technology Behind It</h3>
  <p style="top:234px">Explanation of the technology powering VaultBlocks and how it revolutionizes space infrastructure.</p>
</article>

<h2 class="section-title" style="top:2056px"><span class="rule"></span><span class="accent">Invest</span> in the Cosmic Revolution<span class="rule"></span></h2>
<ul class="ticks abs invest-list">
  <li><svg width="16" height="10" viewBox="0 0 16 10"><path d="M1 5l3 3 6-7M6 8l1 1 8-8" fill="none" stroke="#0054AA" stroke-width="1.3"/></svg><b>Investment Opportunity:</b> A persuasive pitch outlining the investment opportunity, emphasizing potential returns and benefits.</li>
  <li><svg width="16" height="10" viewBox="0 0 16 10"><path d="M1 5l3 3 6-7M6 8l1 1 8-8" fill="none" stroke="#0054AA" stroke-width="1.3"/></svg><b>Financial Insights:</b> Information on market growth, revenue projections, and financial models.</li>
  <li><svg width="16" height="10" viewBox="0 0 16 10"><path d="M1 5l3 3 6-7M6 8l1 1 8-8" fill="none" stroke="#0054AA" stroke-width="1.3"/></svg><b>Investment Process:</b> Step-by-step guide on how potential investors can get involved and support my project.</li>
</ul>

<h2 class="section-title" style="top:2401px"><span class="rule"></span>Journey to the <span class="accent">Stars</span><span class="rule"></span></h2>
<article class="abs post" style="left:121px">
  <div class="pic" role="img" aria-label="Photograph of the Moon over a rocky landscape" style="background:linear-gradient(180deg,#2a2b2e 0%,#141416 100%)"></div>
  <span class="date">01 SEP, 2023</span>
  <p>Lorem Ipsum is simply dummy text of the printing and typesetting industry.</p>
  <span class="go"><svg width="14" height="10" viewBox="0 0 14 10"><path d="M0 5h12M8 1l4 4-4 4" fill="none" stroke="#111821" stroke-width="1.3"/></svg></span>
</article>
<article class="abs post featured" style="left:447px">
  <div class="pic" role="img" aria-label="Photograph of a satellite orbiting Earth" style="background:linear-gradient(180deg,#1c3f6c 0%,#0a1a33 100%)"></div>
  <span class="date">02 SEP, 2023</span>
  <p>Lorem Ipsum is simply dummy text of the printing and typesetting industry.</p>
  <span class="go"><svg width="14" height="10" viewBox="0 0 14 10"><path d="M0 5h12M8 1l4 4-4 4" fill="none" stroke="#0054AA" stroke-width="1.3"/></svg></span>
</article>
<article class="abs post" style="left:775px">
  <div class="pic" role="img" aria-label="Photograph of a spacecraft above Earth with a bright light flare" style="background:linear-gradient(180deg,#17223a 0%,#080d18 100%)"></div>
  <span class="date">03 SEP, 2023</span>
  <p>Lorem Ipsum is simply dummy text of the printing and typesetting industry.</p>
  <span class="go"><svg width="14" height="10" viewBox="0 0 14 10"><path d="M0 5h12M8 1l4 4-4 4" fill="none" stroke="#111821" stroke-width="1.3"/></svg></span>
</article>
<a href="#" class="abs btn btn-pale view-all">View All</a>

<section class="abs community" aria-label="Join the community">
  <h2><span class="rule"></span>Join the Cosmic Community<span class="rule"></span></h2>
  <p>A platform for space enthusiasts, investors,<br>and supporters to engage in discussions and share ideas.</p>
  <div class="signup"><span>Enter Your Email...</span><a href="#" class="btn">Submit</a></div>
</section>

<h2 class="section-title" style="top:3328px"><span class="rule"></span>Let's <span class="accent">Connect</span><span class="rule"></span></h2>
<div class="abs field" style="left:251px;top:3388px;width:338px">Full Name</div>
<div class="abs field" style="left:611px;top:3388px;width:338px">Email Address</div>
<div class="abs field" style="left:251px;top:3440px;width:338px">Phone Number</div>
<div class="abs field" style="left:611px;top:3440px;width:338px">Subjects</div>
<div class="abs field msg" style="left:251px;top:3493px;width:698px">Your Message...</div>
<a href="#" class="abs btn btn-blue send">Submit</a>

<footer>
  <div class="abs footer"></div>
  <div class="abs footer-brand"><span class="brand-mark"></span>Meridian<br>Vault</div>
  <div class="abs socials"><span></span><span class="on"></span><span></span><span></span></div>
  <div class="abs quick" style="left:365px;top:3810px">
    <h3>Quick Links <span class="rule"></span></h3>
    <ul>
      <li><a href="#">Home</a></li><li><a href="#">About Us</a></li>
      <li><a href="#">Gallery</a></li><li><a href="#">Products</a></li>
      <li><a href="#">Projects</a></li><li><a href="#">Our Vision</a></li>
      <li><a href="#">Investment</a></li><li><a href="#">Blog</a></li>
      <li><a href="#">Testimonials</a></li><li><a href="#">Contact Us</a></li>
    </ul>
  </div>
  <div class="abs map" role="img" aria-label="Map showing the company location in northern England"></div>
  <div class="abs legal">
    <span>© 2023 <a href="#">Meridian Vault</a>. All Rights Reserved.</span>
    <span class="faint">Disclaimers: Any necessary disclaimers or legal notices.</span>
    <span class="links">Privacy Policy | Terms of Use | Analytics | Security</span>
  </div>
</footer>

</body>
</html>
```